Business Cards

We are wanting business cards created using previous design #36167008 as a starting point.
Info needed on front side:
Employee Name
Title
Email
Phone Number

Info needed on back side: (these are our product lines)
Frac Valves Fishing
Flowback Thru-Tubing
Torque & Test KMVB

please see changes

```html
<!DOCTYPE html>
<html lang="en">
<head>
<meta charset="utf-8">
<title>Kestrel Downhole – Business Cards</title>
<link href="https://fonts.googleapis.com/css2?family=Montserrat:wght@300;400;500;700&family=Cinzel:wght@500&display=swap" rel="stylesheet">
<style>
  :root {
    --backdrop: #a6a6a6;
    --card: #1b1b1b;
    --gold: #e0c49a;
    --ring: #a8906b;
    --white: #ffffff;
    --ink: #1b1b1b;
  }
  * { margin: 0; padding: 0; box-sizing: border-box; }
  html, body { width: 1200px; height: 1200px; overflow: hidden; }
  body {
    background: var(--backdrop);
    font-family: "Montserrat", Arial, sans-serif;
    position: relative;
  }
  .card {
    position: absolute;
    width: 790px;
    height: 474px;
    background: var(--card);
  }
  .card--front { left: 214px; top: 115px; }
  .card--back { left: 216px; top: 646px; height: 472px; }

  .brand-mark {
    position: absolute;
    border: 10px solid var(--ring);
    border-radius: 50%;
  }
  .brand-name {
    position: absolute;
    text-align: center;
    color: var(--gold);
    font-weight: 700;
    line-height: 1.05;
    text-transform: uppercase;
  }
  .brand-name .line-main { display: block; letter-spacing: 2px; }
  .brand-name .line-sub { display: block; letter-spacing: 3px; }

  /* front */
  .card--front .brand-mark { left: 189px; top: 40px; width: 146px; height: 146px; }
  .card--front .brand-name--kestrel { left: 140px; top: 196px; width: 244px; }
  .card--front .brand-name--kestrel .line-main { font-size: 36px; }
  .card--front .brand-name--kestrel .line-sub { font-size: 20px; margin-top: 4px; }
  .card--front .brand-name--summit { left: 404px; top: 112px; width: 240px; }
  .card--front .brand-name--summit .line-main { font-size: 38px; }
  .card--front .brand-name--summit .line-sub { font-size: 13px; margin-top: 6px; }

  .person {
    position: absolute;
    right: 418px;
    top: 322px;
    text-align: right;
  }
  .person-name {
    color: var(--gold);
    font-weight: 700;
    font-size: 26px;
    letter-spacing: 2px;
    text-transform: uppercase;
  }
  .person-title {
    color: var(--white);
    font-weight: 500;
    font-size: 20px;
    margin-top: 6px;
  }
  .divider {
    position: absolute;
    left: 394px;
    top: 326px;
    width: 2px;
    height: 72px;
    background: #4a4339;
  }
  .contacts {
    position: absolute;
    left: 412px;
    top: 323px;
    list-style: none;
  }
  .contacts li {
    display: flex;
    align-items: center;
    height: 25.5px;
    color: var(--white);
    font-weight: 300;
    font-size: 19px;
  }
  .contacts svg { width: 16px; height: 16px; margin-right: 10px; flex: none; }
  .contacts .accent { color: var(--gold); font-weight: 400; }
  .address {
    position: absolute;
    left: 0; right: 0;
    top: 412px;
    text-align: center;
    color: var(--white);
    font-weight: 300;
    font-size: 19px;
  }

  /* back */
  .card--back .brand-mark { left: 230px; top: 118px; width: 118px; height: 118px; }
  .card--back .brand-name--kestrel { left: 178px; top: 240px; width: 222px; }
  .card--back .brand-name--kestrel .line-main { font-size: 30px; }
  .card--back .brand-name--kestrel .line-sub { font-size: 17px; margin-top: 3px; }
  .card--back .brand-name--summit { left: 399px; top: 188px; width: 192px; }
  .card--back .brand-name--summit .line-main { font-size: 31px; }
  .card--back .brand-name--summit .line-sub { font-size: 10.5px; margin-top: 5px; }

  .product-band {
    position: absolute;
    left: 70px;
    top: 318px;
    width: 648px;
    height: 28px;
    background: var(--gold);
    border-radius: 4px;
    display: flex;
    align-items: center;
    justify-content: center;
    gap: 10px;
    font-family: "Cinzel", Georgia, serif;
    font-weight: 500;
    font-size: 17px;
    color: var(--ink);
    white-space: nowrap;
  }
  .product-band .dot {
    width: 8px; height: 8px; border-radius: 50%; background: var(--ink);
  }
</style>
</head>
<body>

<section class="card card--front" aria-label="Card front">
  <div class="brand-mark"></div>
  <div class="brand-name brand-name--kestrel">
    <span class="line-main">Kestrel</span>
    <span class="line-sub">Downhole LLC</span>
  </div>
  <div class="brand-name brand-name--summit">
    <span class="line-main">Summit</span>
    <span class="line-sub">Production Services</span>
  </div>

  <div class="person">
    <p class="person-name">Dean Whitford</p>
    <p class="person-title">Director</p>
  </div>
  <div class="divider"></div>
  <ul class="contacts">
    <li>
      <svg viewBox="0 0 24 24" aria-hidden="true"><path fill="#e0c49a" d="M6.6 10.8a15 15 0 0 0 6.6 6.6l2.2-2.2c.3-.3.7-.4 1-.2 1.1.4 2.3.6 3.6.6.6 0 1 .4 1 1V20c0 .6-.4 1-1 1A17 17 0 0 1 3 4c0-.6.4-1 1-1h3.5c.6 0 1 .4 1 1 0 1.3.2 2.5.6 3.6.1.3 0 .7-.2 1z"/></svg>
      +1 415 555 0148
    </li>
    <li>
      <svg viewBox="0 0 24 24" aria-hidden="true"><path fill="none" stroke="#e0c49a" stroke-width="2" d="M3 6h18v12H3zM3 6l9 7 9-7"/></svg>
      hello@ridgelineco.com
    </li>
    <li>
      <svg viewBox="0 0 24 24" aria-hidden="true"><g fill="none" stroke="#e0c49a" stroke-width="1.8"><circle cx="12" cy="12" r="9"/><path d="M3 12h18M12 3c3 3 3 15 0 18M12 3c-3 3-3 15 0 18"/></g></svg>
      <span>www.<span class="accent">ridgelineco</span>.com</span>
    </li>
  </ul>
  <p class="address">18 Harbour Lane 3rd Floor Leeds LS1 4AB, United Kingdom</p>
</section>

<section class="card card--back" aria-label="Card back">
  <div class="brand-mark"></div>
  <div class="brand-name brand-name--kestrel">
    <span class="line-main">Kestrel</span>
    <span class="line-sub">Downhole LLC</span>
  </div>
  <div class="brand-name brand-name--summit">
    <span class="line-main">Summit</span>
    <span class="line-sub">Production Services</span>
  </div>

  <div class="product-band">
    <span>Frac Valves Fishing</span>
    <span class="dot"></span>
    <span>Flowback Thru-Tubing</span>
    <span class="dot"></span>
    <span>Torque &amp; Test KMVB</span>
  </div>
</section>

</body>
</html>
```